Copper Kettle Auctions business card design with existing logo

Looking for a sleek and sexy design using our current logo

Contact Information for Business Card

Name, address, email, phone, website. Marcus Delvane 482 Brambleton Road Suite 210C Fernbrook VT 11907 Copperkettlebids.net (555)555-0174

```html
<!DOCTYPE html>
<html lang="en">
<head>
<meta charset="utf-8">
<title>Copper Kettle Auctions – Business Card</title>
<link rel="stylesheet" href="https://fonts.googleapis.com/css2?family=Poppins:wght@400;500;700&family=Michroma&display=swap">
<style>
  :root {
    --backdrop: #76757b;
    --card-white: #ffffff;
    --brand-blue: #1f3d78;
    --brand-red: #d21f2a;
    --ink-blue: #1f3d78;
    --silver: #e9ecf2;
  }
  * { box-sizing: border-box; margin: 0; padding: 0; }
  html, body { width: 1200px; height: 900px; overflow: hidden; }
  body {
    background: var(--backdrop);
    font-family: "Poppins", sans-serif;
    position: relative;
  }
  .card {
    position: absolute;
    left: 285px;
    width: 630px;
    height: 360px;
    border-radius: 18px;
    overflow: hidden;
  }
  .card-front { top: 70px; background: var(--card-white); }
  .card-back { top: 470px; background: var(--brand-blue); }

  /* front */
  .corner-tab {
    position: absolute; top: 0; right: 150px;
    width: 34px; height: 20px; background: var(--brand-blue);
  }
  .name-band {
    position: absolute; left: 0; top: 150px;
    width: 300px; height: 38px; background: var(--brand-red);
    display: flex; align-items: center; padding-left: 26px;
  }
  .name-band .person-name {
    color: var(--card-white); font-weight: 700; font-size: 19px;
    letter-spacing: 1px; text-transform: uppercase;
  }
  .brand-lockup {
    position: absolute; right: 40px; top: 44px;
    display: flex; flex-direction: column; align-items: flex-end;
  }
  .brand-row { display: flex; align-items: center; gap: 10px; }
  .brand-dot { width: 30px; height: 30px; border-radius: 50%; background: var(--brand-blue); }
  .brand-name {
    color: var(--brand-red); font-weight: 700; font-size: 22px;
    letter-spacing: 0.5px; text-transform: uppercase; line-height: 1.1;
  }
  .brand-tagline {
    margin-top: 8px; padding: 3px 0;
    border-top: 1.5px solid var(--brand-blue);
    border-bottom: 1.5px solid var(--brand-blue);
    color: var(--brand-blue); font-weight: 500; font-size: 13px; letter-spacing: 3px;
  }
  .rule {
    position: absolute; top: 232px; height: 1.5px;
  }
  .rule-blue { left: 40px; width: 320px; background: var(--brand-blue); }
  .rule-red { left: 360px; width: 230px; background: var(--brand-red); }
  .contact-list {
    position: absolute; left: 40px; top: 250px; list-style: none;
    color: var(--ink-blue); font-size: 15px; line-height: 24px;
  }
  .contact-list li, .address { display: flex; align-items: center; gap: 10px; }
  .contact-list svg, .address svg { flex: none; }
  .address {
    position: absolute; left: 376px; top: 250px;
    color: var(--ink-blue); font-size: 15px; line-height: 22px; align-items: flex-start;
  }
  .address svg { margin-top: 3px; }

  /* back */
  .back-lockup {
    position: absolute; left: 60px; top: 120px;
    display: flex; align-items: center; gap: 18px;
  }
  .back-dot { width: 70px; height: 70px; border-radius: 50%; background: var(--silver); }
  .back-name {
    color: var(--silver); font-weight: 700; font-size: 40px;
    text-transform: uppercase; line-height: 1.05;
  }
  .back-web {
    position: absolute; right: 36px; bottom: 54px;
    font-family: "Michroma", sans-serif; color: var(--card-white);
    font-size: 13px; letter-spacing: 4px; text-transform: uppercase;
  }
</style>
</head>
<body>
  <section class="card card-front">
    <div class="corner-tab"></div>
    <div class="brand-lockup">
      <div class="brand-row">
        <span class="brand-dot"></span>
        <span class="brand-name">Copper Kettle<br>Auctions</span>
      </div>
      <div class="brand-tagline">BUY-SELL-CONSIGN</div>
    </div>
    <div class="name-band"><span class="person-name">Marcus Delvane</span></div>
    <div class="rule rule-blue"></div>
    <div class="rule rule-red"></div>
    <ul class="contact-list">
      <li>
        <svg width="14" height="14" viewBox="0 0 24 24"><path fill="#d21f2a" d="M6.6 10.8a15 15 0 006.6 6.6l2.2-2.2a1 1 0 011-.25 11.4 11.4 0 003.6.57 1 1 0 011 1V20a1 1 0 01-1 1A17 17 0 013 4a1 1 0 011-1h3.5a1 1 0 011 1c0 1.25.2 2.45.57 3.6a1 1 0 01-.25 1z"/></svg>
        <span>(555)555-0174</span>
      </li>
      <li>
        <svg width="14" height="14" viewBox="0 0 24 24"><rect x="2" y="5" width="20" height="14" rx="1" fill="#d21f2a"/><path d="M2 6l10 7 10-7" stroke="#fff" stroke-width="1.6" fill="none"/></svg>
        <span>info@Copperkettlebids.net</span>
      </li>
      <li>
        <svg width="14" height="14" viewBox="0 0 24 24"><circle cx="12" cy="12" r="10" fill="#d21f2a"/><path d="M2 12h20M12 2c3 3 3 17 0 20M12 2c-3 3-3 17 0 20" stroke="#fff" stroke-width="1.3" fill="none"/></svg>
        <span>Copperkettlebids.net</span>
      </li>
    </ul>
    <div class="address">
      <svg width="14" height="18" viewBox="0 0 24 32"><path fill="#d21f2a" d="M12 0a11 11 0 00-11 11c0 8 11 21 11 21s11-13 11-21A11 11 0 0012 0zm0 15a4 4 0 110-8 4 4 0 010 8z"/></svg>
      <span>482 Brambleton Road<br>Suite 210C Fernbrook<br>VT 11907</span>
    </div>
  </section>

  <section class="card card-back">
    <div class="back-lockup">
      <span class="back-dot"></span>
      <span class="back-name">Copper Kettle<br>Auctions</span>
    </div>
    <div class="back-web">www.copperkettlebids.net</div>
  </section>
</body>
</html>
```